Company notecard redesign

We'd like a redesign done of our company notecards. We use these cards to hand-write messages to clients/potential clients. This could be thank-you cards, congratulations cards, check-in cards, etc. Current cards are 5.5" x 8.5" and fold in half (you'll see the fold mark on the scanned image). We would like the new cards to not fold, and just be 5.5" x 4.25". We do like the little dog head you'll see on the inside notecard scan as the dog is our logo. I've also attached our "professional" logo with our new tagline. Address info you see on the outside notecard scan is correct.

Target Market(s)

Brindlequay and CRM clients

Industry/Entity Type

It Company

Colors
3377b5
ffffff
fff8ef

Requirements
Must have
• Our logo, some contact info
Nice to have
• Dog head from our current notecard scan

```html
<!DOCTYPE html>
<html lang="en">
<head>
<meta charset="utf-8">
<title>Harlow Notecard</title>
<link rel="stylesheet" href="https://fonts.googleapis.com/css2?family=Roboto+Condensed:wght@400;700&family=Roboto:wght@400&display=swap">
<style>
  :root {
    --backdrop: #d3d2d5;
    --navy: #022e4a;
    --sky: #79a7c3;
    --mist: #a7bccb;
    --paper: #f1f1f1;
    --white: #ffffff;
  }
  html, body {
    margin: 0;
    padding: 0;
    overflow: hidden;
  }
  .canvas {
    position: relative;
    width: 1200px;
    height: 991px;
    background: var(--backdrop);
    overflow: hidden;
  }
  .card {
    position: absolute;
    left: 342px;
    width: 518px;
    height: 400px;
    overflow: hidden;
  }
  .card--front {
    top: 70px;
    background: var(--navy);
  }
  .card--back {
    top: 522px;
    background: var(--paper);
  }
  .brand-wrap {
    position: absolute;
    left: 0;
    right: 0;
    top: 174px;
    text-align: center;
  }
  .brand {
    display: inline-block;
    text-align: left;
  }
  .brand__row {
    display: flex;
    align-items: center;
    gap: 6px;
  }
  .brand__name {
    font-family: "Roboto Condensed", sans-serif;
    font-weight: 700;
    font-size: 46px;
    line-height: 1;
    letter-spacing: 1px;
    color: var(--white);
    text-transform: uppercase;
  }
  .brand__dot {
    flex: 0 0 34px;
    width: 34px;
    height: 34px;
    border-radius: 50%;
    background: var(--sky);
  }
  .brand__tagline {
    margin-top: 6px;
    margin-left: 2px;
    font-family: "Roboto", sans-serif;
    font-size: 9.5px;
    letter-spacing: 0.9px;
    color: var(--mist);
    white-space: nowrap;
    text-transform: uppercase;
  }
  .contact {
    position: absolute;
    left: 0;
    right: 0;
    top: 350px;
    text-align: center;
    font-family: "Roboto Condensed", sans-serif;
    font-size: 9.5px;
    line-height: 12px;
    color: var(--white);
  }
  .contact__web-name {
    color: var(--sky);
  }
  .corner-mascot {
    position: absolute;
    left: 410px;
    top: 296px;
    width: 108px;
    height: 104px;
    background: var(--sky);
    border-top-left-radius: 60px 56px;
  }
</style>
</head>
<body>
  <main class="canvas">
    <section class="card card--front">
      <div class="brand-wrap">
        <div class="brand">
          <div class="brand__row">
            <span class="brand__name">Harlow</span>
            <span class="brand__dot"></span>
          </div>
          <div class="brand__tagline">A Cloud Consulting Company</div>
        </div>
      </div>
      <div class="contact">
        <div>1180 N Westfield Ave, Carmel, Indiana 46032 · T: 317.555.0148</div>
        <div>www.<span class="contact__web-name">HARLOWTECH</span>.com</div>
      </div>
    </section>
    <section class="card card--back">
      <div class="corner-mascot" role="img" aria-label="Light blue dog head mascot illustration in profile, cropped at the bottom right corner"></div>
    </section>
  </main>
</body>
</html>
```